New Web Design Project

Details for my new Web Design Project will be added soon.
Updates
This is my website that need to be work into it www.brambleworthquest.com
I am really frustrated with your company, we really need a refund of $556.00 as soon as possible, Do not feel safe to work with.

```html
<!DOCTYPE html>
<html lang="en">
<head>
<meta charset="utf-8">
<title>Brambleworth Quest — Online Store</title>
<link rel="stylesheet" href="https://fonts.googleapis.com/css2?family=Roboto:wght@300;400;500;700&display=swap">
<style>
:root{
  --page:#f4f4f4;
  --ink:#111;
  --black:#0b0b0b;
  --pink:#e5157f;
  --grey:#777;
  --mid:#444;
  --line:#dcdcdc;
  --panel:#fafafa;
  --white:#fff;
}
*{box-sizing:border-box;margin:0;padding:0}
html,body{width:1200px;height:1000px;overflow:hidden}
body{background:var(--page);font-family:"Roboto",Arial,sans-serif;color:var(--ink);position:relative}
.abs{position:absolute}
a{color:inherit;text-decoration:none}

/* top promo strip */
.promo-code{left:644px;top:13px;width:129px;height:24px;background:var(--pink);color:var(--white);font-size:5.5px;font-weight:700;display:flex;align-items:center;justify-content:center}
.promo-discount{left:773px;top:13px;width:110px;height:24px;background:var(--black);color:var(--white);font-size:6.5px;font-weight:700;padding:4px 0 0 21px;line-height:9px}

/* header */
.site-header{left:305px;top:37px;width:578px;height:68px;background:var(--black)}
.brand{left:12px;top:27px;display:flex;align-items:center;gap:5px;color:var(--white);font-size:6px;font-weight:500;line-height:6px;letter-spacing:.3px}
.brand-mark{width:12px;height:12px;background:var(--white)}
.welcome{left:409px;top:22px;color:var(--white);font-size:7px}
.account-links{left:354px;top:39px;color:var(--white);font-size:6px;word-spacing:1px}
.cart-icon{left:509px;top:22px;width:26px;height:24px;background:var(--black);border:1px solid var(--white);display:flex;align-items:center;justify-content:center}
.cart-count{left:535px;top:22px;width:30px;height:24px;background:var(--white);font-size:12px;display:flex;align-items:center;justify-content:center}

/* category sidebar */
.category-panel{left:305px;top:105px;width:133px;height:251px;background:var(--white)}
.panel-title{left:8px;top:13px;width:116px;height:21px;background:var(--black);color:var(--white);font-size:8px;padding:6px 0 0 8px;border-bottom:2px solid var(--pink)}
.category-list{left:8px;top:46px;list-style:none;font-size:5.5px;color:var(--grey);line-height:16.6px;text-transform:uppercase}

/* hero */
.hero-main{left:438px;top:105px;width:207px;height:251px;background:linear-gradient(180deg,#c9b9a4 0%,#8a7c6c 40%,#3a3430 100%)}
.sale-band{left:438px;top:241px;width:207px;height:54px;background:var(--pink)}
.sale-pct{left:448px;top:250px;color:var(--white);font-size:34px;font-weight:300;letter-spacing:-1px;line-height:34px}
.sale-text{left:530px;top:250px;color:var(--white);font-size:15px;font-weight:300;line-height:17px}
.dots{left:586px;top:298px;display:flex;gap:1px}
.dots span{width:7px;height:7px;background:var(--black)}
.dots span:first-child{background:var(--pink)}
.hero-arrival{left:645px;top:105px;width:238px;height:136px;background:linear-gradient(180deg,#9a9a9a,#6a6d6a)}
.arrival-box{left:687px;top:134px;width:158px;height:75px;background:rgba(20,20,20,.88);color:var(--white);text-align:center}
.arrival-box h2{font-size:11px;font-weight:400;line-height:13px;margin-top:13px}
.arrival-box p{font-size:5.5px;line-height:7px;margin-top:4px}
.arrival-arrow{left:811px;top:180px}
.hero-skate{left:645px;top:241px;width:119px;height:115px;background:linear-gradient(180deg,#8c8a88,#3a3a3c)}
.hero-skirt{left:764px;top:241px;width:119px;height:115px;background:linear-gradient(135deg,#5ab3d4,#e45a8c 50%,#f0c24a)}
.collection-band{left:645px;top:295px;width:238px;height:27px;background:rgba(30,30,30,.75)}
.collection-label{color:var(--white);font-size:8px;line-height:9px}

/* special product column */
.special-panel{left:305px;top:356px;width:133px;height:224px;background:var(--mid)}
.special-title{left:8px;top:13px;width:116px;height:22px;background:var(--white);font-size:8px;padding:7px 0 0 8px;border-bottom:2px solid var(--pink)}
.special-image{left:8px;top:44px;width:116px;height:134px;background:linear-gradient(180deg,#e0e0e0 0%,#e0e0e0 8%,#2a1a12 12%,#c2411c 50%,#1c120c 100%)}
.special-name{left:0;top:187px;width:133px;text-align:center;color:var(--white);font-size:6px}
.special-price{left:0;top:199px;width:133px;text-align:center;color:var(--white);font-size:8px}
.promo-ad{left:305px;top:580px;width:133px;height:223px;background:linear-gradient(180deg,#4a7ab8 0%,#3c4e72 40%,#1e2030 100%)}
.ad-bar{left:0;top:114px;width:93px;height:12px;background:var(--white)}
.ad-headline{left:1px;top:126px;color:var(--white);font-weight:700;font-size:25px;line-height:24px;letter-spacing:-.5px}
.ad-sub{left:1px;top:149px;color:var(--white);font-weight:700;font-size:12px}
.ad-note{left:2px;top:166px;color:var(--white);font-size:5px}

/* products */
.product-area{left:438px;top:356px;width:445px;height:447px;background:var(--panel)}
.section-title{font-size:8.5px;color:#555}
.section-chevron{font-size:10px;color:#999}
.product-card{width:123px;height:160px;background:var(--white);border:1px solid var(--line)}
.product-card .photo{position:absolute;left:0;top:0;width:121px;height:117px}
.photo.flame{background:linear-gradient(180deg,#d8d8d8 0%,#2a1a12 10%,#c2411c 55%,#1a110c 100%)}
.photo.skort{background:linear-gradient(180deg,#f2f2f2 0%,#222 25%,#111 100%)}
.photo.hearts{background:linear-gradient(135deg,#f0c24a,#4fb0d6 35%,#e45a8c 65%,#55a8d0)}
.product-card .name{position:absolute;left:0;top:126px;width:121px;text-align:center;font-size:5.5px;color:var(--grey)}
.product-card .price{position:absolute;left:0;top:140px;width:121px;text-align:center;font-size:8px;color:var(--pink)}
.product-card.is-hover{height:209px}
.product-card.is-hover .hover-band{position:absolute;left:0;top:117px;width:121px;height:37px;background:#e8e8e8}
.add-cart{left:13px;top:164px;width:94px;height:20px;background:var(--pink);color:var(--white);font-size:8px;display:flex;align-items:center;padding-left:10px;gap:30px}
.card-actions{left:15px;top:192px;font-size:5.5px;color:var(--grey);word-spacing:1px}

/* footer */
.footer-rule{left:305px;width:578px;height:1px;background:var(--line)}
.follow{left:305px;top:847px;font-size:11px;color:#666}
.social{top:842px;width:22px;height:22px;background:#333}
.divider{top:843px;width:1px;height:22px;background:var(--line)}
.free-ship{left:531px;top:845px;color:var(--pink);font-size:9px}
.ship-code{left:531px;top:857px;color:#555;font-size:6px;font-weight:500}
.order{left:741px;top:849px;font-size:8.5px;color:#666}
.order b{color:var(--pink);font-weight:400}
.foot-col{top:899px}
.foot-col h3{font-size:6.5px;font-weight:700;color:#555;margin-bottom:7px}
.foot-col li{list-style:none;font-size:5.5px;color:#888;line-height:11px}
.newsletter-input{left:749px;top:915px;width:102px;height:19px;background:var(--white);border:1px solid var(--line);font-size:4.5px;color:#777;padding:6px 0 0 5px}
.newsletter-go{left:851px;top:915px;width:32px;height:19px;background:#222;color:var(--white);font-size:7px;display:flex;align-items:center;justify-content:center}
.store-address{left:749px;top:946px;font-size:5.5px;color:#555;line-height:8px}
</style>
</head>
<body>

<div class="abs promo-code">SHIPPING COST: 35% CODE :(BQSAVE2014)!</div>
<div class="abs promo-discount">Discount! $9.99<br>Worldwide Buyers + 35%</div>

<header class="abs site-header">
  <div class="abs brand"><span class="brand-mark"></span><span>BRAMBLEWORTH<br>QUEST</span></div>
  <div class="abs welcome">Welcome to our online store!</div>
  <nav class="abs account-links">My Account &nbsp;| &nbsp; My Wishlist &nbsp;| &nbsp; Checkout &nbsp;| &nbsp; Log In</nav>
  <div class="abs cart-icon">
    <svg width="14" height="12" viewBox="0 0 14 12" fill="none" stroke="#fff" stroke-width="1.3"><path d="M0 1h2.5l2 7h7l1.5-5H4"/><circle cx="5.5" cy="10.5" r="1" fill="#fff"/><circle cx="10.5" cy="10.5" r="1" fill="#fff"/></svg>
  </div>
  <div class="abs cart-count">0</div>
</header>

<aside class="abs category-panel">
  <div class="abs panel-title">ALL CATEGORIES</div>
  <ul class="abs category-list">
    <li>Competition Ice Figure Skating Dress</li>
    <li>Shorts &amp; Skirts</li>
    <li>How to Measure</li>
    <li>Ice Figure Skating Accessories</li>
    <li>Ice Figure Skating Practice Dress</li>
    <li>Gymnastic</li>
    <li>Yoga Pant</li>
    <li>Community</li>
    <li>Ice Figure Skating Pants</li>
    <li>Boy &amp; Men Ice Figure Skating Pants</li>
    <li>Skating Pant &amp; Jacket</li>
    <li>Coupon</li>
  </ul>
</aside>

<section class="hero">
  <div class="abs hero-main" role="img" aria-label="Model wearing a black skating top and pants"></div>
  <div class="abs sale-band"></div>
  <div class="abs sale-pct">-50%</div>
  <div class="abs sale-text">CLEARANCE<br>SALE</div>
  <div class="abs dots"><span></span><span></span><span></span><span></span></div>

  <div class="abs hero-arrival" role="img" aria-label="Dark green hooded jackets with pink trim"></div>
  <div class="abs arrival-box">
    <h2>NEW<br>ARRIVAL</h2>
    <p>Lorem ipsum dolor sit amet,<br>consectetur adipisicing elit</p>
  </div>
  <svg class="abs arrival-arrow" width="8" height="12" viewBox="0 0 8 12"><path d="M1 1l5 5-5 5" fill="none" stroke="#e5157f" stroke-width="1.3"/></svg>

  <div class="abs hero-skate" role="img" aria-label="Black skating skirt worn over leggings"></div>
  <div class="abs hero-skirt" role="img" aria-label="Colourful heart print sports skirt"></div>
  <div class="abs collection-band"></div>
  <div class="abs collection-label" style="left:655px;top:299px">ICE FIGURE<br>COLLECTION</div>
  <div class="abs collection-label" style="left:773px;top:301px">SPORTS<br>SKIRTS</div>
  <div class="abs collection-label" style="left:805px;top:298px;font-size:18px;line-height:18px">&amp;</div>
</section>

<aside>
  <div class="abs special-panel">
    <div class="abs special-title">SPECIAL PRODUCT</div>
    <div class="abs special-image" role="img" aria-label="Flame print yoga pants"></div>
    <div class="abs special-name">FIRE FLAMMY YOGA PANT BQYP01</div>
    <div class="abs special-price">$ 49.99</div>
  </div>
  <div class="abs promo-ad" role="img" aria-label="Model in a black lace dress on a city street at night">
    <div class="abs ad-bar"></div>
    <div class="abs ad-headline">40% OFF</div>
    <div class="abs ad-sub">ONLINE ONLY!</div>
    <div class="abs ad-note">EVERY SINGLE ITEM. <b>FREE SHIPPING.</b></div>
  </div>
</aside>

<main class="abs product-area">
  <div class="abs section-title" style="left:20px;top:18px">Featured Products</div>
  <div class="abs section-chevron" style="left:414px;top:15px">›</div>

  <div class="abs product-card" style="left:19px;top:40px">
    <div class="photo flame" role="img" aria-label="Flame print yoga pants"></div>
    <div class="name">FIRE FLAMMY YOGA PANT BQYP01</div><div class="price">$ 49.99</div>
  </div>
  <div class="abs product-card is-hover" style="left:160px;top:40px">
    <div class="photo skort" role="img" aria-label="Black skating skirt over leggings"></div>
    <div class="hover-band"></div>
    <div class="name">FIRE FLAMMY YOGA PANT BQYP01</div><div class="price">$ 49.99</div>
    <div class="abs add-cart"><span>Add to Cart</span>
      <svg width="14" height="12" viewBox="0 0 14 12" fill="none" stroke="#fff" stroke-width="1.3"><path d="M0 1h2.5l2 7h7l1.5-5H4"/><circle cx="5.5" cy="10.5" r="1" fill="#fff"/><circle cx="10.5" cy="10.5" r="1" fill="#fff"/></svg>
    </div>
    <div class="abs card-actions">▪ Compare &nbsp;&nbsp;&nbsp; ▪ Add to Wishlist</div>
  </div>
  <div class="abs product-card" style="left:299px;top:40px">
    <div class="photo hearts" role="img" aria-label="Heart print sports skirt"></div>
    <div class="name">FIRE FLAMMY YOGA PANT BQYP01</div><div class="price">$ 49.99</div>
  </div>

  <div class="abs section-title" style="left:20px;top:242px">New Products</div>
  <div class="abs section-chevron" style="left:414px;top:239px">›</div>

  <div class="abs product-card" style="left:19px;top:263px">
    <div class="photo flame" role="img" aria-label="Flame print yoga pants"></div>
    <div class="name">FIRE FLAMMY YOGA PANT BQYP01</div><div class="price">$ 49.99</div>
  </div>
  <div class="abs product-card" style="left:160px;top:263px">
    <div class="photo skort" role="img" aria-label="Black skating skirt over leggings"></div>
    <div class="name">FIRE FLAMMY YOGA PANT BQYP01</div><div class="price">$ 49.99</div>
  </div>
  <div class="abs product-card" style="left:299px;top:263px">
    <div class="photo hearts" role="img" aria-label="Heart print sports skirt"></div>
    <div class="name">FIRE FLAMMY YOGA PANT BQYP01</div><div class="price">$ 49.99</div>
  </div>
</main>

<footer>
  <div class="abs footer-rule" style="top:835px"></div>
  <div class="abs footer-rule" style="top:872px"></div>
  <div class="abs follow">FOLLOW US</div>
  <div class="abs social" style="left:389px" aria-label="Community page"></div>
  <div class="abs social" style="left:415px" aria-label="Updates feed"></div>
  <div class="abs divider" style="left:486px"></div>
  <div class="abs free-ship">FREE SHIPPING</div>
  <div class="abs ship-code">SHIPPING COST: 35% CODE :(BQSAVE2014)</div>
  <div class="abs divider" style="left:707px"></div>
  <div class="abs order">ORDER ONLINE &nbsp;<b>TEL: 1234 5678 001</b></div>

  <div class="abs foot-col" style="left:305px"><h3>MY ACCOUNT</h3><ul><li>Sign In</li><li>View Cart</li><li>My Wishlist</li><li>Track My Order</li><li>Help</li></ul></div>
  <div class="abs foot-col" style="left:463px"><h3>SITE INFO</h3><ul><li>About Us</li><li>Customer Service</li><li>Privacy Policy</li><li>Site Map</li><li>Search Terms</li><li>Advanced Search</li><li>Orders and Returns</li></ul></div>
  <div class="abs foot-col" style="left:606px"><h3>WHY BUY FOR US</h3><ul><li>Shipping &amp; Returns</li><li>Secure Shopping</li><li>International Shipping</li><li>Affiliates</li><li>Group Sales</li><li>Contact Us</li></ul></div>
  <div class="abs foot-col" style="left:749px"><h3>NEWSLETTER</h3></div>
  <div class="abs newsletter-input">Enter Your Email Address</div>
  <div class="abs newsletter-go">Go</div>
  <div class="abs store-address">Store Location: #1234, Lorem Ipsum Link<br>Lorem Ipsum, 2345</div>
</footer>

</body>
</html>
```